Upmarket, mysterious, eye-catching box design for oral care product.

Teeth are like crops in the fields; and gums play the same role as fields. If fields are not irrigated and fertilized properly, crops cannot be harvested. So, logistically, if gums are not healthy, we cannot have healthy teeth. Our product are bottles of herbal nutrition to feed our customers’ gums. Every drop of our product is previous for oral care, especially for the health of gums. I wish you guys could source out characteristics of our product and build them up by designs.

Before you start your job, pls remember my analogy and let your designs fly in imagination.

Target Market(s)

female from 18 to 50

Industry/Entity Type

oral care

Requirements
Must have
• good taste
Nice to have
• imagination

```html
<!DOCTYPE html>
<html lang="en">
<head>
<meta charset="utf-8">
<title>Aligner Gel Box</title>
<link rel="stylesheet" href="https://fonts.googleapis.com/css2?family=Montserrat:wght@600;700;800&display=swap">
<style>
  :root {
    --green: #2f7d32;
    --green-deep: #1d5a20;
    --green-light: #4f9e4b;
    --leaf-tint: rgba(170, 220, 160, 0.22);
    --ink: #2c6b2f;
    --white: #ffffff;
    --stage: #ffffff;
  }
  * { margin: 0; padding: 0; box-sizing: border-box; }
  html, body { width: 1200px; height: 917px; overflow: hidden; background: var(--stage); }
  body { position: relative; font-family: "Montserrat", Arial, sans-serif; }

  .dieline { position: absolute; left: 270px; top: 70px; width: 660px; height: 780px; display: flex; }

  .panel { position: relative; height: 100%; overflow: hidden; background: var(--green); }
  .panel--side { width: 220px; }
  .panel--side::after { content: ""; position: absolute; inset: 0; box-shadow: inset -8px 0 14px rgba(0,0,0,0.14); pointer-events: none; }
  .panel--front { width: 440px; }

  .leaf-pattern { position: absolute; inset: 0;
    background:
      radial-gradient(ellipse 38% 22% at 30% 72%, var(--leaf-tint), transparent 70%),
      radial-gradient(ellipse 30% 18% at 70% 46%, var(--leaf-tint), transparent 70%),
      radial-gradient(ellipse 26% 16% at 22% 40%, rgba(170,220,160,0.16), transparent 70%),
      radial-gradient(ellipse 34% 20% at 60% 88%, rgba(170,220,160,0.14), transparent 70%),
      linear-gradient(180deg, var(--green-light) 0%, var(--green) 45%, var(--green-deep) 100%); }
  .panel--side .leaf-pattern {
    background:
      radial-gradient(ellipse 45% 20% at 40% 55%, var(--leaf-tint), transparent 70%),
      radial-gradient(ellipse 40% 18% at 55% 82%, rgba(170,220,160,0.16), transparent 70%),
      linear-gradient(180deg, var(--green-light) 0%, var(--green) 45%, var(--green-deep) 100%); }

  .side-top { position: absolute; left: 0; top: 0; width: 100%; height: 200px; background: var(--white); }
  .side-tagline { position: absolute; top: 46px; left: 0; width: 100%; text-align: center;
    font-size: 14px; font-weight: 700; line-height: 1.35; color: var(--ink); }

  .features { position: absolute; top: 255px; left: 18px; right: 14px; list-style: none; }
  .feature { display: flex; align-items: center; gap: 8px; margin-bottom: 58px; }
  .feature-icon { width: 44px; height: 44px; flex-shrink: 0; }
  .feature-text { font-size: 12px; font-weight: 700; line-height: 1.3; color: var(--white); text-transform: uppercase; }

  .front-wave { position: absolute; left: 0; top: 0; width: 100%; height: 250px; }

  .brand { position: absolute; top: 66px; left: 0; width: 100%; display: flex; justify-content: center; align-items: center; gap: 10px; }
  .brand-name { font-size: 40px; font-weight: 800; color: var(--ink); letter-spacing: -1px; }
  .brand-dot { width: 14px; height: 14px; border-radius: 50%; background: var(--ink); }

  .product { position: absolute; top: 352px; left: 30px; color: var(--white); }
  .product-name { font-size: 88px; font-weight: 800; line-height: 0.92; letter-spacing: -2px; }
  .product-row { display: flex; align-items: flex-start; gap: 12px; }
  .product-type { font-size: 88px; font-weight: 800; line-height: 0.92; letter-spacing: -2px;
    border-right: 3px solid var(--white); padding-right: 10px; }
  .product-sub { font-size: 20px; font-weight: 700; line-height: 1.25; padding-top: 10px; }

  .volume { position: absolute; bottom: 80px; width: 100%; text-align: center;
    font-size: 19px; font-weight: 600; color: var(--white); }
</style>
</head>
<body>
  <main class="dieline">
    <section class="panel panel--side">
      <div class="leaf-pattern" role="img" aria-label="Faint botanical leaf and vine pattern on green"></div>
      <div class="side-top">
        <p class="side-tagline">Immune Support for<br>Oral Health</p>
      </div>
      <ul class="features">
        <li class="feature">
          <svg class="feature-icon" viewBox="0 0 44 44" role="img" aria-label="Aligner tray icon" fill="none" stroke="#fff" stroke-width="2" stroke-linecap="round">
            <path d="M6 20 C8 32 16 36 22 36 C28 36 36 32 38 20"/>
            <path d="M11 21 C13 29 18 31 22 31 C26 31 31 29 33 21"/>
            <path d="M16 10 L13 15 M22 8 V14 M28 10 L31 15"/>
          </svg>
          <span class="feature-text">Reduce pain<br>from aligners</span>
        </li>
        <li class="feature">
          <svg class="feature-icon" viewBox="0 0 44 44" role="img" aria-label="Clean tooth icon" fill="none" stroke="#fff" stroke-width="2" stroke-linecap="round" stroke-linejoin="round">
            <path d="M14 12 C10 12 8 16 9 21 C10 26 12 28 13 34 C14 38 17 38 18 34 L20 27 L22 34 C23 38 26 38 27 34 C28 28 30 26 31 21 C32 16 30 12 26 12 C24 12 22 14 20 14 C18 14 16 12 14 12 Z"/>
            <path d="M36 4 V12 M32 8 H40"/>
          </svg>
          <span class="feature-text">Maintain<br>dental hygiene</span>
        </li>
        <li class="feature">
          <svg class="feature-icon" viewBox="0 0 44 44" role="img" aria-label="Strong tooth icon" fill="none" stroke="#fff" stroke-width="2" stroke-linecap="round" stroke-linejoin="round">
            <path d="M17 14 C13 14 11 18 12 23 C13 28 15 30 16 36 C17 40 20 40 21 36 L22 29 L24 36 C25 40 28 40 29 36 C30 30 32 28 33 23 C34 18 32 14 28 14 C26 14 24 16 22.5 16 C21 16 19 14 17 14 Z"/>
            <path d="M12 20 H5 V10 H9 M33 20 H40 V10 H36"/>
          </svg>
          <span class="feature-text">Strengthen<br>gums</span>
        </li>
      </ul>
    </section>

    <section class="panel panel--front">
      <div class="leaf-pattern" role="img" aria-label="Faint botanical leaf and vine pattern on green"></div>
      <svg class="front-wave" viewBox="0 0 440 250" preserveAspectRatio="none" aria-hidden="true">
        <path d="M0 0 H440 V150 C380 210 290 160 200 175 C120 190 50 212 0 205 Z" fill="#ffffff"/>
      </svg>
      <div class="brand">
        <span class="brand-name">verda drop</span>
        <span class="brand-dot"></span>
      </div>
      <div class="product">
        <div class="product-name">Aligner</div>
        <div class="product-row">
          <span class="product-type">gel</span>
          <span class="product-sub">Herbal Extracts<br>and Formulas</span>
        </div>
      </div>
      <p class="volume">30ml E</p>
    </section>
  </main>
</body>
</html>
```